Education provider needs a landing page for its brand

We need a landing page for an advertising campaign that we are currently running on jobtrawl.com.au.
We're Fernbrook Institute. We offer Australian online qualifications (courses) that help people get jobs with the right knowledge.
We'd like a landing page that shows our quirky, fun style that breaks away from traditional, conservative education advertising. The final landing page needs to be a strong converter for leads as it can take up to 90 days for someone to decide to study a course.
Check out our website. www.fernbrook.edu.au

We also like the attached landing pages by Zolt and Pellow Academy.

Target Market(s)

25-45 yr olds who have recently searched for a course to study on Trawl.

Font styles to use
Sans Serif

Colors
3276b5
85acd3
ecf5f6
87d0c7

Requirements
Must have
• - Simple and uncluttered
- Logo
- Video - https://vidhost.example/qT7mWx2LcaB
- 3 x dot points about why Fernbrook is your best educator partner
- It needs a lead form to capture user's details so we can nurture them in an email campaign. This will be a 'Learn More' button that allows them to add their name and email address and they will be sent information.
- 'Enrol Now' button
Nice to have
• - Simple list of courses that we offer

```html
<!DOCTYPE html>
<html lang="en">
<head>
<meta charset="utf-8">
<title>Fernbrook Institute – Landing Page</title>
<link href="https://fonts.googleapis.com/css2?family=Source+Sans+3:ital,wght@0,400;0,600;0,700;1,400&display=swap" rel="stylesheet">
<style>
:root{
  --teal:#2ed3c6;
  --teal-btn:#22dccb;
  --green:#3ccf8a;
  --navy:#234a63;
  --navy-deep:#1f4a66;
  --blue:#3276b5;
  --blue-soft:#85acd3;
  --mist:#ecf5f6;
  --ink:#1d1d1f;
  --grey:#666;
  --field:#eeeeee;
  --white:#fff;
}
*{margin:0;padding:0;box-sizing:border-box}
html,body{width:1200px;height:3518px;overflow:hidden}
body{position:relative;background:var(--white);font-family:"Source Sans 3",Arial,sans-serif;color:var(--ink)}
.abs{position:absolute}
.stage-band{left:0;top:0;width:1200px;height:691px;background:var(--teal)}
.page{left:95px;top:126px;width:1008px;height:3289px;background:var(--white);box-shadow:0 10px 40px rgba(0,0,0,.18)}

/* hero */
.hero{left:95px;top:126px;width:1008px;height:565px;background:linear-gradient(180deg,#2f9ea3 0%,#2a7f8f 55%,#224f69 100%)}
.logo{left:229px;top:126px;width:85px;height:83px;background:var(--navy);color:var(--white);display:flex;flex-direction:column;align-items:center;justify-content:flex-end;padding-bottom:10px;font-weight:600;line-height:1.05;text-align:center}
.logo .sq{width:22px;height:22px;background:var(--white);margin-bottom:8px}
.logo .name{font-size:11px;letter-spacing:.5px}
.logo .sub{font-size:7px;letter-spacing:1px}
.phone{left:771px;top:143px;color:var(--white);font-size:19px;font-weight:600;display:flex;align-items:center;gap:6px}
.menu{left:938px;top:148px;width:32px}
.menu span{display:block;height:5px;border-radius:3px;background:var(--white);margin-bottom:5px}
.menu span:nth-child(2){width:26px;margin-left:6px}
.lead-form{left:229px;top:254px;width:335px;height:381px;background:var(--white);border-top:10px solid var(--blue-soft)}
.lead-form h2{margin-top:28px;text-align:center;color:var(--green);font-size:15px;line-height:19px;font-weight:700}
.field{position:absolute;left:32px;width:271px;height:32px;background:var(--field);font-size:9px;color:#666;padding:11px 16px;text-transform:uppercase}
.submit{position:absolute;left:32px;top:313px;width:271px;height:33px;background:var(--teal-btn);color:var(--white);font-weight:700;font-size:15px;text-align:center;line-height:33px}
.hero-photo{left:587px;top:225px;width:423px;height:466px;background:radial-gradient(ellipse at 60% 45%,#d8c7b7 0%,#8a6a55 35%,rgba(42,110,130,0) 70%)}

/* different */
.diff-accent{left:232px;top:743px;width:75px;height:80px;background:var(--teal)}
.diff-photo-a{left:247px;top:758px;width:197px;height:200px;background:linear-gradient(135deg,#c9b8a3,#7b6a5b);box-shadow:0 4px 12px rgba(0,0,0,.2)}
.diff-photo-b{left:401px;top:846px;width:138px;height:137px;background:linear-gradient(135deg,#e1b14a,#8c6d4a);border:3px solid var(--white);box-shadow:0 4px 12px rgba(0,0,0,.25)}
.diff-title{left:640px;top:737px;font-size:23px;font-weight:700}
.diff-intro{left:647px;top:778px;width:330px;font-size:10.5px;line-height:13px;color:var(--grey)}
.ticks{left:640px;top:825px;list-style:none;font-size:10.5px;color:var(--grey)}
.ticks li{position:absolute;left:0;width:320px;padding-left:26px;line-height:13px}
.ticks li::before{content:"";position:absolute;left:0;top:3px;width:9px;height:9px;border-radius:50%;background:var(--green)}

/* benefits band */
.benefits{left:95px;top:1047px;width:1008px;height:341px;background:linear-gradient(180deg,#2f566f,#3d6682 60%,#355d76)}
.ring{width:224px;height:224px;border-radius:50%;border:1.5px solid rgba(255,255,255,.45);display:flex;align-items:center;justify-content:center}
.ring .disc{width:188px;height:188px;border-radius:50%;display:flex;flex-direction:column;align-items:center;justify-content:center;color:var(--white);font-size:12px;line-height:15px;text-align:center}
.link-line{top:1212px;height:1px;background:rgba(255,255,255,.5)}

/* courses */
.courses-title{left:0;width:1200px;top:1436px;text-align:center;font-size:23px;font-weight:700}
.card{background:var(--white);box-shadow:0 2px 10px rgba(0,0,0,.1);font-size:12.5px;line-height:14px;text-align:center;display:flex;flex-direction:column;align-items:center;justify-content:center;gap:12px}
.card.row{flex-direction:row;text-align:left;gap:12px}

/* online */
.online-box{left:229px;top:1785px;width:740px;height:271px;background:var(--navy)}
.online-photo{left:545px;top:1765px;width:390px;height:317px;background:linear-gradient(135deg,#d6d8d6,#8f8a86 55%,#5a5656);box-shadow:0 6px 18px rgba(0,0,0,.3)}
.online-title{left:250px;top:1818px;font-size:24px;font-weight:700;color:var(--white)}
.online-intro{left:252px;top:1853px;width:270px;font-size:9px;line-height:11px;color:#dce6ec}
.online-list{left:252px;top:1890px;list-style:none;font-size:11px;color:#e8eef2}
.online-list li{position:absolute;left:0;width:280px;padding-left:28px;white-space:nowrap}
.online-list li::before{content:"";position:absolute;left:2px;top:4px;width:9px;height:9px;border-radius:50%;background:var(--green)}
.btn-touch{left:251px;top:1992px;width:100px;height:23px;background:var(--teal-btn);color:var(--white);font-size:12px;line-height:23px;text-align:center}

/* rank */
.rank{left:95px;top:2133px;width:1008px;height:306px;background:linear-gradient(90deg,#3a6b86,#4d7b94 50%,#3a6884)}
.rank-title{left:0;width:1200px;top:2160px;text-align:center;font-size:23px;font-weight:700;color:var(--white)}
.rank-intro{left:380px;width:440px;top:2197px;text-align:center;font-size:9px;line-height:12px;color:#e1eaf0}
.stat{width:200px;text-align:center;color:var(--white)}
.stat svg{display:block;margin:0 auto 8px}
.stat p{font-size:15px;line-height:19px}

/* video */
.video{left:231px;top:2490px;width:738px;height:318px;background:linear-gradient(90deg,#4d4640,#8a6a58 45%,#3c4a30 80%,#2c3a24)}
.play{left:559px;top:2623px}

/* testimonial */
.t-accent{left:231px;top:2857px;width:83px;height:51px;background:var(--teal)}
.t-photo{left:247px;top:2873px;width:247px;height:221px;background:linear-gradient(135deg,#c8a35e,#6d5a46 60%,#2b2b2b);box-shadow:0 4px 14px rgba(0,0,0,.2)}
.t-quote-box{left:429px;top:3023px;width:98px;height:90px;background:var(--blue-soft);display:flex;align-items:center;justify-content:center}
.t-text{left:550px;top:2899px;width:400px;font-size:15.5px;line-height:22px;font-style:italic;color:#333}
.t-name{left:550px;top:3032px;font-size:15px;font-weight:700;color:var(--green)}
.t-role{left:550px;top:3055px;font-size:10px;color:#444}
.dot{top:3123px;width:12px;height:12px;border-radius:50%;border:1.5px solid #bbb}
.dot.on{background:var(--green);border-color:var(--green)}

/* footer */
.footer{left:95px;top:3185px;width:1008px;height:230px;background:var(--navy-deep);color:#c4d3dd}
.f-logo{left:232px;top:3245px;width:40px;height:41px;background:#15324a;color:var(--white);font-size:6px;font-weight:600;text-align:center;display:flex;flex-direction:column;align-items:center;justify-content:flex-end;padding-bottom:5px}
.f-logo .sq{width:10px;height:10px;background:var(--white);margin-bottom:4px}
.f-about{left:232px;top:3298px;width:190px;font-size:10px;line-height:15px}
.f-head{top:3244px;font-size:12px;color:var(--white);letter-spacing:.3px}
.f-text{top:3271px;font-size:10px;line-height:15px;width:160px}
.socials{left:457px;top:3319px;display:flex;gap:26px}
.socials span{width:13px;height:13px;border-radius:50%;background:#9fb3c2}
.f-input{left:632px;top:3320px;width:183px;height:30px;background:#e8eef2;font-size:8.5px;color:#555;padding:10px 18px}
.f-btn{left:863px;top:3320px;width:103px;height:30px;border:1px solid #8fb0c8;background:#5a7d98;color:#e9f0f4;font-size:8.5px;text-align:center;line-height:28px}
.f-copy{left:235px;top:3381px;font-size:9px}
.f-policy{left:909px;top:3381px;font-size:9px}
.side-chat{left:1073px;top:3234px;width:30px;height:28px;background:#2f7fc0}
.side-mail{left:1073px;top:3263px;width:30px;height:28px;background:#e0403f}
</style>
</head>
<body>
<div class="abs stage-band"></div>
<div class="abs page"></div>

<header>
  <div class="abs hero"></div>
  <div class="abs hero-photo" role="img" aria-label="Smiling student in glasses holding a pen and a colourful notebook, giving a thumbs up"></div>
  <div class="abs logo"><span class="sq"></span><span class="name">FERNBROOK</span><span class="sub">INSTITUTE</span></div>
  <div class="abs phone">
    <svg width="14" height="14" viewBox="0 0 24 24"><path d="M6.6 10.8a15 15 0 0 0 6.6 6.6l2.2-2.2c.3-.3.7-.4 1-.2 1.1.4 2.3.6 3.6.6.6 0 1 .4 1 1V20c0 .6-.4 1-1 1A17 17 0 0 1 3 4c0-.6.4-1 1-1h3.5c.6 0 1 .4 1 1 0 1.3.2 2.5.6 3.6.1.3 0 .7-.2 1z" fill="#2ed3c6"/></svg>
    1300 555 014
  </div>
  <div class="abs menu" aria-label="Menu"><span></span><span></span><span></span></div>

  <form class="abs lead-form">
    <h2>ARE YOU LOOKING THE BEST<br>ADUCATION INSTITUTE</h2>
    <div class="field" style="top:73px">Name</div>
    <div class="field" style="top:122px">Email ID</div>
    <div class="field" style="top:173px">Subject</div>
    <div class="field" style="top:223px;height:71px">Message</div>
    <div class="submit">SUBMIT NOW</div>
  </form>
</header>

<section>
  <div class="abs diff-accent"></div>
  <div class="abs diff-photo-a" role="img" aria-label="Two students laughing together over a laptop"></div>
  <div class="abs diff-photo-b" role="img" aria-label="Student in a yellow shirt with a backpack giving a thumbs up"></div>
  <h2 class="abs diff-title">What makes us different?</h2>
  <p class="abs diff-intro">You've found it! This is where we keep all the important info that students need to know about Fernbrook Institute.</p>
  <ul class="abs ticks">
    <li style="top:0">Learn skills that are relevant</li>
    <li style="top:30px">Australia's highest-rated private training institute</li>
    <li style="top:60px">Last year Fernbrook Institute trained more tax agents and bookkeepers than any other private institute</li>
    <li style="top:101px">Fast turnaround on assessments</li>
    <li style="top:131px">Support at times that you need it</li>
  </ul>
</section>

<section>
  <div class="abs benefits" role="img" aria-label="Dimmed photo of a hand writing in a notebook"></div>
  <div class="abs link-line" style="left:452px;width:34px"></div>
  <div class="abs link-line" style="left:710px;width:34px"></div>
  <div class="abs ring" style="left:228px;top:1100px"><div class="disc" style="background:#1fb5a6">
    <svg width="58" height="50" viewBox="0 0 58 50" fill="none" stroke="#fff" stroke-width="2"><circle cx="29" cy="14" r="6"/><path d="M17 44v-8a12 12 0 0 1 24 0v8z"/><circle cx="12" cy="10" r="3"/><circle cx="46" cy="10" r="3"/><circle cx="8" cy="30" r="3"/><circle cx="50" cy="30" r="3"/></svg>
    <p style="margin-top:8px">Get the skills that<br>employers really want.</p></div></div>
  <div class="abs ring" style="left:486px;top:1100px"><div class="disc" style="background:#4f93c9">
    <svg width="58" height="50" viewBox="0 0 58 50" fill="none" stroke="#fff" stroke-width="2"><path d="M29 48V18M29 18l-14-10M29 18l14-10M29 4v14"/><path d="M10 8h6v6M48 8h-6v6M26 7l3-4 3 4"/></svg>
    <p style="margin-top:8px">Absolute flexibility.<br>Your way, your terms.</p></div></div>
  <div class="abs ring" style="left:744px;top:1100px"><div class="disc" style="background:#8fb9de">
    <svg width="50" height="44" viewBox="0 0 50 44" fill="none" stroke="#fff" stroke-width="2"><rect x="6" y="10" width="26" height="26"/><path d="M6 17h26"/><circle cx="36" cy="12" r="9"/><path d="M36 7v5l3 2"/></svg>
    <p style="margin-top:8px">Unrivalled support.<br>Delivered with care.</p></div></div>
</section>

<section>
  <h2 class="abs courses-title">Our papular Courses</h2>
  <div class="abs card" style="left:229px;top:1502px;width:178px;height:125px"><svg width="36" height="36"><rect x="4" y="2" width="22" height="30" fill="none" stroke="#3276b5" stroke-width="2"/><circle cx="26" cy="24" r="7" fill="none" stroke="#3276b5" stroke-width="2"/></svg><span>Accounting &amp;<br>Bookkeeping</span></div>
  <div class="abs card" style="left:416px;top:1502px;width:178px;height:125px"><svg width="36" height="36"><path d="M4 32V22M12 32V16M20 32V12M28 32V6" stroke="#3276b5" stroke-width="3"/></svg><span>Financial<br>Planning</span></div>
  <div class="abs card" style="left:603px;top:1502px;width:179px;height:125px"><svg width="36" height="36"><circle cx="10" cy="10" r="5" fill="none" stroke="#f08a3c" stroke-width="2"/><circle cx="26" cy="10" r="5" fill="none" stroke="#f08a3c" stroke-width="2"/><rect x="4" y="20" width="28" height="12" fill="none" stroke="#f08a3c" stroke-width="2"/></svg><span>Business &amp;<br>Management</span></div>
  <div class="abs card" style="left:792px;top:1502px;width:177px;height:125px"><svg width="36" height="36"><rect x="4" y="4" width="16" height="10" fill="none" stroke="#8a5bd1" stroke-width="2"/><circle cx="28" cy="24" r="5" fill="none" stroke="#8a5bd1" stroke-width="2"/><path d="M12 14v12h10" stroke="#8a5bd1" stroke-width="2" stroke-dasharray="2 2" fill="none"/></svg><span>Transport &amp;<br>Logistics</span></div>

  <div class="abs card row" style="left:229px;top:1638px;width:142px;height:79px"><svg width="34" height="34"><rect x="3" y="6" width="20" height="24" fill="none" stroke="#2fa37a" stroke-width="2"/><circle cx="24" cy="22" r="8" fill="none" stroke="#2fa37a" stroke-width="2"/></svg><span>Finance&amp;<br>Martgage<br>Broke</span></div>
  <div class="abs card row" style="left:379px;top:1638px;width:142px;height:79px"><svg width="34" height="34"><path d="M3 12L17 4l14 8z M5 14v14M12 14v14M22 14v14M29 14v14M3 30h28" fill="none" stroke="#8bc34a" stroke-width="2"/></svg><span>Governance</span></div>
  <div class="abs card row" style="left:530px;top:1638px;width:142px;height:79px"><svg width="34" height="34"><rect x="3" y="4" width="12" height="10" fill="none" stroke="#f2c53d" stroke-width="2"/><rect x="19" y="4" width="12" height="10" fill="none" stroke="#f2c53d" stroke-width="2"/><rect x="3" y="20" width="12" height="10" fill="none" stroke="#f2c53d" stroke-width="2"/><circle cx="25" cy="25" r="5" fill="none" stroke="#f2c53d" stroke-width="2"/></svg><span>Marketing</span></div>
  <div class="abs card row" style="left:678px;top:1638px;width:142px;height:79px"><svg width="34" height="34"><rect x="4" y="6" width="24" height="22" fill="none" stroke="#e8679a" stroke-width="2"/><path d="M4 13h24M10 18h12M10 23h8" stroke="#e8679a" stroke-width="2"/></svg><span>Project<br>managment</span></div>
  <div class="abs card row" style="left:829px;top:1638px;width:140px;height:79px"><svg width="34" height="34"><circle cx="17" cy="9" r="5" fill="none" stroke="#6f5bc9" stroke-width="2"/><path d="M8 30a9 9 0 0 1 18 0M2 30a6 6 0 0 1 8-6M32 30a6 6 0 0 0-8-6" fill="none" stroke="#6f5bc9" stroke-width="2"/></svg><span>Human<br>Resources</span></div>
</section>

<section>
  <div class="abs online-box"></div>
  <div class="abs online-photo" role="img" aria-label="Three students looking at a laptop together"></div>
  <h2 class="abs online-title">Studying online</h2>
  <p class="abs online-intro">Lorem ipsum dolor sit amet, consectetur adipiscing elit, sed do eiusmod tempor incididunt ut labore et</p>
  <ul class="abs online-list">
    <li style="top:0">How does studying online actually work?</li>
    <li style="top:21px">What is it like?</li>
    <li style="top:43px">How does studying online actually work?</li>
    <li style="top:64px">What about student support?</li>
  </ul>
  <div class="abs btn-touch">Get in Touch</div>
</section>

<section>
  <div class="abs rank" role="img" aria-label="Dimmed photo of smiling students"></div>
  <h2 class="abs rank-title">How we rank</h2>
  <p class="abs rank-intro">Every month we measure our student's feedback. This keeps us on our toes, so our courses and support stay ahead of the pack. Here's what they have to say this month...</p>
  <div class="abs stat" style="left:288px;top:2254px">
    <svg width="92" height="92" viewBox="0 0 92 92"><circle cx="46" cy="46" r="43" fill="none" stroke="rgba(255,255,255,.35)" stroke-width="3"/><circle cx="46" cy="46" r="43" fill="none" stroke="#fff" stroke-width="3" stroke-dasharray="246 270" transform="rotate(-90 46 46)"/><text x="46" y="53" fill="#fff" font-size="21" text-anchor="middle" font-family="Source Sans 3,sans-serif">91%</text></svg>
    <p>Would recommend<br>to a friend</p></div>
  <div class="abs stat" style="left:499px;top:2254px">
    <svg width="92" height="92" viewBox="0 0 92 92"><circle cx="46" cy="46" r="43" fill="none" stroke="rgba(255,255,255,.35)" stroke-width="3"/><circle cx="46" cy="46" r="43" fill="none" stroke="#2ed3c6" stroke-width="3" stroke-dasharray="227 270" transform="rotate(-90 46 46)"/><text x="46" y="53" fill="#fff" font-size="21" text-anchor="middle" font-family="Source Sans 3,sans-serif">84%</text></svg>
    <p>Are satisfied with<br>the training</p></div>
  <div class="abs stat" style="left:711px;top:2254px">
    <svg width="92" height="92" viewBox="0 0 92 92"><circle cx="46" cy="46" r="43" fill="none" stroke="rgba(255,255,255,.35)" stroke-width="3"/><circle cx="46" cy="46" r="43" fill="none" stroke="#3ccf8a" stroke-width="3" stroke-dasharray="240 270" transform="rotate(-90 46 46)"/><text x="46" y="53" fill="#fff" font-size="21" text-anchor="middle" font-family="Source Sans 3,sans-serif">89%</text></svg>
    <p>Are happy with our<br>responsiveness</p></div>
</section>

<section>
  <div class="abs video" role="img" aria-label="Video still of a man speaking in front of plants"></div>
  <svg class="abs play" width="50" height="50" viewBox="0 0 50 50"><circle cx="25" cy="25" r="23" fill="none" stroke="#fff" stroke-width="3"/><path d="M20 15l13 10-13 10z" fill="#fff"/></svg>
</section>

<section>
  <div class="abs t-accent"></div>
  <div class="abs t-photo" role="img" aria-label="Smiling woman in glasses working on a laptop"></div>
  <div class="abs t-quote-box"><svg width="46" height="34" viewBox="0 0 46 34" fill="none" stroke="#fff" stroke-width="3"><path d="M4 3h14v16l-6 12H6l5-12H4zM26 3h14v16l-6 12h-6l5-12h-7z"/></svg></div>
  <p class="abs t-text">It was really fun getting to know the team during the project. They were all helpful in answering my questions and made me feel completely at ease.The design ended&nbsp; up being twice as good as I could have ever envisioned!</p>
  <p class="abs t-name">Priya Nandan</p>
  <p class="abs t-role">Co founder, Group</p>
  <span class="abs dot on" style="left:563px"></span>
  <span class="abs dot" style="left:592px"></span>
  <span class="abs dot" style="left:621px"></span>
  <span class="abs dot" style="left:649px"></span>
</section>

<footer>
  <div class="abs footer"></div>
  <div class="abs f-logo"><span class="sq"></span>FERNBROOK</div>
  <p class="abs f-about">Lorem ipsum dolor sit amet, consec tetur adipiscing elit, sed do eiusmod tempor incididunt ut labore et dolo.</p>
  <p class="abs f-head" style="left:457px">CONNECT PEOPLE</p>
  <p class="abs f-text" style="left:457px">Connect with us and stay<br>in the loop.</p>
  <div class="abs socials" aria-label="Social links"><span></span><span></span><span></span><span></span></div>
  <p class="abs f-head" style="left:635px">EMAIL UPDATES</p>
  <p class="abs f-text" style="left:635px">Be the first to hear about our<br>Event announcements.</p>
  <div class="abs f-input">Enter your email id
    <svg style="position:absolute;right:14px;top:8px" width="16" height="14" viewBox="0 0 16 14"><path d="M0 6L16 0 11 14 8 8z" fill="#7a8b97"/></svg></div>
  <p class="abs f-head" style="left:864px">CONTACT US</p>
  <p class="abs f-text" style="left:864px">Question? We've got<br>answer. Try us.</p>
  <div class="abs f-btn">EMAIL US</div>
  <p class="abs f-copy">© 2020. ALL RIGHTS RESERVED.</p>
  <p class="abs f-policy">Privacy Policy</p>
  <div class="abs side-chat"><svg width="30" height="28"><rect x="8" y="7" width="14" height="10" rx="2" fill="#fff"/><path d="M11 17v4l4-4" fill="#fff"/></svg></div>
  <div class="abs side-mail"><svg width="30" height="28"><rect x="8" y="8" width="14" height="11" fill="#fff"/><path d="M8 8l7 6 7-6" stroke="#e0403f" fill="none" stroke-width="1.5"/></svg></div>
</footer>
</body>
</html>
```